Design a poster that illustrates the six central pillars of our school district's efforts with students. The attached PDF outlines the six main competencies we aim for students to possess upon graduation. Each of the 6 has 3 bullet points for the poster as well. The title is "Profile of a Kestrel". Our mascot is this attached winged wheel. The overall concept is that staff take kids when they are young and develop these 6 things when they graduate. Our colors are navy, red, and white. We will make this poster in a variety of sizes in offices, classrooms, and in digital spaces as well. On the PDF - ignore the column that says "Synthesis". That has nothing to do with this poster.

The district is Harlow Creek Public Schools https://www.harlowcreek-schools.example/

```html
<!DOCTYPE html>
<html lang="en">
<head>
<meta charset="utf-8">
<title>Profile of a Kestrel</title>
<link rel="stylesheet" href="https://fonts.googleapis.com/css2?family=Archivo+Black&family=Barlow+Condensed:wght@500;600&display=swap">
<style>
  :root {
    --backdrop: #bdbec0;
    --navy: #0d0d3d;
    --red: #a01e24;
    --white: #ffffff;
  }
  * { margin: 0; padding: 0; box-sizing: border-box; }
  html, body {
    width: 924px;
    height: 1200px;
    overflow: hidden;
    background: var(--backdrop);
  }
  .poster {
    position: absolute;
    left: 90px;
    top: 74px;
    width: 744px;
    height: 1051px;
    background: var(--navy);
    overflow: hidden;
  }
  .masthead {
    position: absolute;
    left: 0;
    top: 0;
    width: 100%;
    height: 176px;
    background: var(--red);
  }
  .mascot-mark {
    position: absolute;
    left: 95px;
    top: 46px;
    display: flex;
    align-items: center;
    gap: 12px;
  }
  .mascot-mark .dot {
    width: 58px;
    height: 58px;
    border-radius: 50%;
    background: var(--navy);
  }
  .mascot-mark .name {
    font-family: "Barlow Condensed", sans-serif;
    font-weight: 600;
    font-size: 44px;
    color: var(--white);
    line-height: 1;
  }
  .title {
    position: absolute;
    left: 340px;
    top: 58px;
    font-family: "Archivo Black", sans-serif;
    color: var(--white);
    line-height: 1;
  }
  .title .kicker {
    display: block;
    font-size: 37px;
    letter-spacing: 1.5px;
  }
  .title .name {
    display: block;
    font-size: 63px;
    margin-top: 4px;
    letter-spacing: 0.5px;
  }
  .pillar {
    position: absolute;
    width: 308px;
    height: 220px;
    border: 2.5px solid var(--red);
    border-radius: 14px;
  }
  .pillar h2 {
    position: absolute;
    left: 20px;
    top: -22px;
    padding: 0 5px;
    background: var(--navy);
    font-family: "Barlow Condensed", sans-serif;
    font-weight: 600;
    font-size: 31px;
    line-height: 36px;
    color: var(--white);
  }
  .pillar ul {
    list-style: none;
    position: absolute;
    left: 12px;
    right: 8px;
    top: 24px;
    font-family: "Barlow Condensed", sans-serif;
    font-weight: 600;
    font-size: 19px;
    line-height: 22px;
    letter-spacing: -0.5px;
    color: var(--white);
  }
  .pillar li {
    position: relative;
    padding-left: 12px;
    margin-bottom: 12px;
  }
  .pillar li:last-child { margin-bottom: 0; }
  .pillar li::before {
    content: "";
    position: absolute;
    left: 0;
    top: 8px;
    width: 5px;
    height: 5px;
    border-radius: 50%;
    background: var(--white);
  }
  .pillar.spaced li { margin-bottom: 20px; }
  .pillar.spaced li:last-child { margin-bottom: 0; }
  .col-left { left: 48px; }
  .col-right { left: 388px; }
  .row-1 { top: 232px; }
  .row-2 { top: 505px; }
  .row-3 { top: 777px; }
</style>
</head>
<body>
  <main class="poster">
    <header class="masthead">
      <div class="mascot-mark">
        <span class="dot"></span>
        <span class="name">Kestrel</span>
      </div>
      <h1 class="title">
        <span class="kicker">PROFILE OF A</span>
        <span class="name">KESTREL</span>
      </h1>
    </header>

    <section class="pillar col-left row-1">
      <h2>Communicator</h2>
      <ul>
        <li>Expresses ideas clearly and respectfully (written &amp; verbal).</li>
        <li>Listens actively and understands diverse perspectives.</li>
        <li>Adjusts communication to suit the audience and context.</li>
      </ul>
    </section>

    <section class="pillar col-right row-1">
      <h2>Critical Thinker</h2>
      <ul>
        <li>Questions, analyzes, and evaluates information from multiple sources.</li>
        <li>Identifies and solves complex problems creatively.</li>
        <li>Uses evidence and diverse perspectives to form reasoned conclusions and make informed</li>
      </ul>
    </section>

    <section class="pillar spaced col-left row-2">
      <h2>Responsible</h2>
      <ul>
        <li>Takes ownership of actions, choices, and commitments.</li>
        <li>Manages time, resources, and self to meet expectations.</li>
        <li>Acts with integrity and advocates for self and others.</li>
      </ul>
    </section>

    <section class="pillar col-right row-2">
      <h2>Adaptable</h2>
      <ul>
        <li>Responds productively to new situations, challenges, and feedback.</li>
        <li>Learns from new experiences and applies prior knowledge in evolving contexts.</li>
        <li>Adjusts behavior and approach to effectively engage with diverse groups and environments.</li>
      </ul>
    </section>

    <section class="pillar col-left row-3">
      <h2>Collaborator</h2>
      <ul>
        <li>Contributes effectively and cooperatively to shared goals</li>
        <li>Listens actively and values diverse ideas and perspectives.</li>
        <li>Engages respectfully, compromising and leading when appropriate.</li>
      </ul>
    </section>

    <section class="pillar col-right row-3">
      <h2>Compassionate</h2>
      <ul>
        <li>Understands and acknowledges others' feelings, perspectives, and experiences.</li>
        <li>Responds with kindness, patience, and support.</li>
        <li>Seeks to connect with and contribute positively to the well-being of others</li>
      </ul>
    </section>
  </main>
</body>
</html>
```